Label design for Essential Oil Bottle

We need a logo and label design for our range of medical essential oils. We distill our own oils in very stringent conditions and run various analysis per batch. That is what sets us apart from other essential oil retailers. Our brand name is 'Velmiro', which is the shortened name for Sacred Frankincense.

The design should communicate the following qualities:

1. Nature
2. Clinical
3. Professional
4. Advanced

Please keep the design minimal and clean.

We like the colours gold, maroon, white. Essential oil bottle will be 15 ml amber bottle

Types of oil: Orange, Rose, Frankincense, Myrrh

Do keep in mind that this same brand will also have a range of skin care.
Updates

Hi all,

Just a reminder that the label should be landscape and not portrait. The label is meant to wrap around the 15 ml amber bottle. Photo of the bottle is attached in the brief.

thanksĀ 

Target Market(s)

Clinicians, Laboratories, General public

Industry/Entity Type

Medical

Requirements
Must have
• Front:

Logo
Oil name
Latin name (in smaller italized font)
Volume: 0.5 oz/15 ml

Back:

Barcode
Batch code
Expiry date
Company name/address: Velmiro Inc. 5678 Quarry Ln, Los Angeles, CA

```html
<!DOCTYPE html>
<html lang="en">
<head>
<meta charset="utf-8">
<title>Velmiro Medical Essential Oils – Label Range</title>
<link rel="stylesheet" href="https://fonts.googleapis.com/css2?family=Arimo:ital,wght@0,400;0,700;1,400&display=swap">
<style>
  :root{
    --maroon:#8e1b33;
    --ink:#2b2b2b;
    --stage-top:#ffffff;
    --stage-bottom:#e4e4e4;
    --swoosh:#d9cbb0;
    --orange:#f0921c;
    --orange-tint:#fbf6ee;
    --rose:#e8508e;
    --rose-tint:#fbeff4;
    --frank:#8d8d8d;
    --frank-tint:#f1f1f1;
    --myrrh:#f3c600;
    --myrrh-tint:#fbf7e6;
  }
  *{box-sizing:border-box;margin:0;padding:0}
  html,body{width:1200px;height:900px;overflow:hidden}
  body{
    font-family:"Arimo",Arial,sans-serif;
    background:radial-gradient(ellipse at 50% 35%,var(--stage-top) 0%,var(--stage-bottom) 100%);
    position:relative;
  }
  .label-range{position:absolute;top:425px;left:0;width:1200px;height:315px}
  .label{
    position:absolute;top:0;width:242px;height:315px;
    border-top:6px solid var(--accent);
    border-bottom:6px solid var(--accent);
    text-align:center;overflow:hidden;
  }
  .label--orange{left:68px;--accent:var(--orange);--tint:var(--orange-tint);--title:var(--orange)}
  .label--rose{left:338px;--accent:var(--rose);--tint:var(--rose-tint);--title:var(--rose)}
  .label--frank{left:612px;--accent:var(--frank);--tint:var(--frank-tint);--title:var(--ink)}
  .label--myrrh{left:886px;--accent:var(--myrrh);--tint:var(--myrrh-tint);--title:var(--maroon)}
  .label__pattern{position:absolute;inset:0;background:var(--tint)}
  .label__content{position:relative;height:100%}
  .label__origin{
    position:absolute;top:34px;left:0;right:0;
    font-size:11px;font-weight:700;color:var(--ink);letter-spacing:.3px
  }
  .label__origin-country{color:var(--maroon);font-size:13px}
  .label__arc{position:absolute;top:44px;left:0;width:242px;height:60px}
  .label__arc text{font-family:"Arimo",Arial,sans-serif;font-size:11px;font-weight:700;letter-spacing:.6px}
  .label__latin{
    position:absolute;top:84px;left:0;right:0;
    font-size:8px;font-style:italic;color:var(--ink);letter-spacing:.3px
  }
  .label__brand{
    position:absolute;top:95px;left:0;right:0;
    font-size:43px;font-weight:400;color:var(--maroon);letter-spacing:-1px;line-height:50px
  }
  .label__swoosh{position:absolute;top:92px;left:0;width:242px;height:70px}
  .label__oil{
    position:absolute;top:204px;left:50%;transform:translateX(-50%);
    background:var(--accent);color:#fff;
    font-size:9.5px;letter-spacing:1px;padding:1px 14px;border-radius:7px;white-space:nowrap
  }
  .label__process{
    position:absolute;top:231px;left:0;right:0;
    font-size:11px;font-weight:700;letter-spacing:.7px;color:var(--title)
  }
  .label__volume{
    position:absolute;top:265px;left:0;right:0;
    font-size:16px;font-weight:700;color:var(--title)
  }
  .label--orange .label__process,.label--orange .label__volume{color:#eaa54a}
  .label--rose .label__process,.label--rose .label__volume{color:var(--maroon)}
  .label--myrrh .label__process,.label--myrrh .label__volume{color:#c9a23a}
</style>
</head>
<body>
<main class="label-range">

  <section class="label label--orange">
    <div class="label__pattern" role="img" aria-label="Faint floral line pattern in pale orange"></div>
    <div class="label__content">
      <p class="label__origin">Origin: <span class="label__origin-country">India</span></p>
      <svg class="label__arc" viewBox="0 0 242 60"><path id="arc-orange" d="M40 46 Q121 20 202 46" fill="none"/><text fill="#f4b04f"><textPath href="#arc-orange" startOffset="50%" text-anchor="middle">Medical Essential Oils</textPath></text></svg>
      <p class="label__latin">Boswellia Carterii</p>
      <svg class="label__swoosh" viewBox="0 0 242 70"><path d="M30 40 Q121 90 212 40" fill="none" stroke="var(--swoosh)" stroke-width="1.5"/></svg>
      <h2 class="label__brand">Velmiro</h2>
      <p class="label__oil">Orange Extract</p>
      <p class="label__process">Hydro distilled in the US</p>
      <p class="label__volume">15 ml</p>
    </div>
  </section>

  <section class="label label--rose">
    <div class="label__pattern" role="img" aria-label="Faint floral line pattern in pale pink"></div>
    <div class="label__content">
      <p class="label__origin">Origin: <span class="label__origin-country">India</span></p>
      <svg class="label__arc" viewBox="0 0 242 60"><path id="arc-rose" d="M40 46 Q121 20 202 46" fill="none"/><text fill="var(--rose)"><textPath href="#arc-rose" startOffset="50%" text-anchor="middle">Medical Essential Oils</textPath></text></svg>
      <p class="label__latin">Boswellia Carterii</p>
      <svg class="label__swoosh" viewBox="0 0 242 70"><path d="M30 40 Q121 90 212 40" fill="none" stroke="var(--swoosh)" stroke-width="1.5"/></svg>
      <h2 class="label__brand">Velmiro</h2>
      <p class="label__oil">Rose Extract</p>
      <p class="label__process">Hydro distilled in the US</p>
      <p class="label__volume">15 ml</p>
    </div>
  </section>

  <section class="label label--frank">
    <div class="label__pattern" role="img" aria-label="Faint floral line pattern in pale grey"></div>
    <div class="label__content">
      <p class="label__origin">Origin: <span class="label__origin-country">India</span></p>
      <svg class="label__arc" viewBox="0 0 242 60"><path id="arc-frank" d="M40 46 Q121 20 202 46" fill="none"/><text fill="var(--ink)"><textPath href="#arc-frank" startOffset="50%" text-anchor="middle">Medical Essential Oils</textPath></text></svg>
      <p class="label__latin">Boswellia Carterii</p>
      <svg class="label__swoosh" viewBox="0 0 242 70"><path d="M30 40 Q121 90 212 40" fill="none" stroke="var(--swoosh)" stroke-width="1.5"/></svg>
      <h2 class="label__brand">Velmiro</h2>
      <p class="label__oil">Frankincense</p>
      <p class="label__process">Hydro distilled in the US</p>
      <p class="label__volume">15 ml</p>
    </div>
  </section>

  <section class="label label--myrrh">
    <div class="label__pattern" role="img" aria-label="Faint floral line pattern in pale yellow"></div>
    <div class="label__content">
      <p class="label__origin">Origin: <span class="label__origin-country">India</span></p>
      <svg class="label__arc" viewBox="0 0 242 60"><path id="arc-myrrh" d="M40 46 Q121 20 202 46" fill="none"/><text fill="var(--maroon)"><textPath href="#arc-myrrh" startOffset="50%" text-anchor="middle">Medical Essential Oils</textPath></text></svg>
      <p class="label__latin">Boswellia Carterii</p>
      <svg class="label__swoosh" viewBox="0 0 242 70"><path d="M30 40 Q121 90 212 40" fill="none" stroke="var(--swoosh)" stroke-width="1.5"/></svg>
      <h2 class="label__brand">Velmiro</h2>
      <p class="label__oil" style="color:var(--maroon)">Myrrh Extract</p>
      <p class="label__process">Hydro distilled in the US</p>
      <p class="label__volume">15 ml</p>
    </div>
  </section>

</main>
</body>
</html>
```